Print design needed to improve the layout and look of some existing documents

We need someone to take a couple of existing documents that we have and make them look much better using our existing logo and corporate colors etc. We require these to be delivered in a format that will allow our staff to edit the content as necessary via Microsoft word for conversion once finalized into a PDF. Ideally, we will also be able to use this as a newsletter template or for other documents that might be required in our business. www.calderfinch.com.au
Updates

Project Deadline Extended Reason: So far, I have only seen one design that I believe is quite good quality. Added Sunday, July 3, 2016

Target Market(s)

Business owners, executives, retirees

Industry/Entity Type

Financial Service

Font styles to use
Serif

Requirements
Must have
• Design that uses our existing branding and colors. It also needs to be ina form that we can edit the content / update easily. Ideally the format / layout could also be used for other documents such as short newsletters etc.
Nice to have
• Fresh, simple and crisp. Very professional looking.
Should not have
• strange fonts, weird layouts.

```html
<!DOCTYPE html>
<html lang="en">
<head>
<meta charset="utf-8">
<title>Calder Finch Private Wealth – Newsletter</title>
<link rel="stylesheet" href="https://fonts.googleapis.com/css2?family=Open+Sans:wght@400;600;700;800&family=Source+Sans+3:wght@400;600&display=swap">
<style>
  :root {
    --ink: #111111;
    --brand-blue: #3e76a6;
    --brand-green: #7ac143;
    --nav-dark: #3e76a6;
    --nav-light: #6bb3e0;
    --sea-deep: #4d7aa6;
    --sea-mid: #86a9c6;
    --sea-light: #c9d8e4;
    --sand: #b9b2a6;
    --card-text: #4a4a4a;
    --paper: #ffffff;
  }
  * { box-sizing: border-box; margin: 0; padding: 0; }
  html, body { width: 848px; height: 1200px; overflow: hidden; background: var(--paper); }
  .page { position: relative; width: 848px; height: 1200px; font-family: "Source Sans 3", Arial, sans-serif; color: var(--ink); }

  .brand { position: absolute; left: 110px; top: 46px; display: flex; align-items: center; gap: 14px; }
  .brand-mark { width: 30px; height: 30px; background: var(--brand-green); }
  .brand-name { font-family: "Open Sans", Arial, sans-serif; font-weight: 600; font-size: 27px; line-height: 1; color: var(--brand-blue); }

  .hero-sea { position: absolute; left: 100px; top: 119px; width: 642px; height: 224px;
    background: linear-gradient(180deg, var(--sea-deep) 0%, var(--sea-mid) 30%, var(--sea-light) 52%, var(--sea-mid) 68%, var(--sand) 100%); }
  .hero-photo { position: absolute; left: 533px; top: 35px; width: 181px; height: 234px;
    background: linear-gradient(160deg, #e9e6e2 0%, #c9b6a6 50%, #4f86c2 100%); border: 2px solid #ffffff; }

  .company-card { position: absolute; left: 131px; top: 148px; width: 330px; height: 106px;
    background: rgba(255,255,255,0.55); padding: 20px 8px 0 0; text-align: right; font-style: normal;
    font-family: "Open Sans", Arial, sans-serif; font-size: 9.6px; line-height: 14px; color: var(--card-text); font-weight: 600; }

  .services { position: absolute; left: 100px; top: 287px; width: 642px; height: 151px; display: flex; }
  .service { flex: 1; display: flex; flex-direction: column; align-items: center; }
  .service.dark { background: var(--nav-dark); }
  .service.light { background: var(--nav-light); }
  .service-title { height: 62px; padding-top: 4px; text-align: center; color: #ffffff;
    font-family: "Open Sans", Arial, sans-serif; font-weight: 700; font-size: 10.6px; line-height: 13.5px; }
  .service-thumb { width: 71px; height: 71px; border: 2px solid #ffffff; }
  .thumb-desk { background: linear-gradient(135deg, #f4f4f4, #b7bcc2); }
  .thumb-office { background: linear-gradient(180deg, #eef0f2, #b98a6e); }
  .thumb-meeting { background: linear-gradient(180deg, #3f8a5c, #37404e); }
  .thumb-people { background: linear-gradient(180deg, #8fb7d8, #b8473f); }
  .thumb-chairs { background: linear-gradient(135deg, #e6edf0, #9aa3a6); }

  .article { position: absolute; left: 100px; width: 642px; display: flex; }
  .article-thumb { width: 81px; height: 79px; flex: none; margin-top: 3px;
    background: linear-gradient(180deg, var(--sea-deep) 0%, var(--sea-mid) 45%, var(--sea-light) 70%, var(--sea-mid) 100%); }
  .article-body { margin-left: 42px; width: 510px; }
  .article-title { font-family: "Open Sans", Arial, sans-serif; font-weight: 700; font-size: 24px; line-height: 28px; margin-bottom: 1px; }
  .article-text { font-size: 16.6px; line-height: 21.6px; }

  .footer-sea { position: absolute; left: 100px; top: 1102px; width: 642px; height: 50px;
    background: linear-gradient(180deg, var(--sea-deep) 0%, var(--sea-mid) 50%, var(--sea-deep) 100%); }
</style>
</head>
<body>
<div class="page">

  <header class="brand">
    <span class="brand-mark"></span>
    <span class="brand-name">Calder Finch Private Wealth</span>
  </header>

  <div class="hero-sea" role="img" aria-label="Calm beach with blue sea and sand"></div>
  <div class="hero-photo" role="img" aria-label="Smiling retired couple embracing"></div>

  <address class="company-card">
    Calder Finch Wealth Pty Ltd &nbsp;|&nbsp; AFSL 508214 &nbsp;|&nbsp; ABN 51 702 318 446<br>
    42 Harlow Street, Eastview, WA 6150<br>
    PO Box 2284, Westbrook WA 6150<br>
    www.calderfinch.com.au<br>
    Tel.: 08 6400 2718
  </address>

  <nav class="services">
    <div class="service dark">
      <div class="service-title">MY PORTFOLIO<br>Comprehensive<br>Investment<br>Management</div>
      <div class="service-thumb thumb-desk" role="img" aria-label="Desk with paperwork"></div>
    </div>
    <div class="service light">
      <div class="service-title">WEALTH CREATION<br>Six Step<br>Process To<br>Financial Planning</div>
      <div class="service-thumb thumb-office" role="img" aria-label="Office meeting table"></div>
    </div>
    <div class="service dark">
      <div class="service-title">SMSF's<br>Self-managed<br>Superannuation<br>Fund</div>
      <div class="service-thumb thumb-meeting" role="img" aria-label="Advisers in a meeting"></div>
    </div>
    <div class="service light">
      <div class="service-title">PHILANTHROPIC<br>for people<br>of WA</div>
      <div class="service-thumb thumb-people" role="img" aria-label="Group of community volunteers"></div>
    </div>
    <div class="service dark">
      <div class="service-title">AGEING<br>WITH ASSETS</div>
      <div class="service-thumb thumb-chairs" role="img" aria-label="Empty boardroom chairs"></div>
    </div>
  </nav>

  <article class="article" style="top:464px">
    <div class="article-thumb" role="img" aria-label="Blue sea texture"></div>
    <div class="article-body">
      <h2 class="article-title">LOREM IPSUM</h2>
      <p class="article-text">Lorem ipsum dolor sit amet, consectetur adipiscing elit. Etiam accumsan ac erat in consequat. Pellentesque at ligula a lacus elementum pellente&shy;sque nec eget tortor. Maecenas convallis dolor sit amet eros consequat, vitae faucibus arcu pharetra. Quisque vitae fermentum lorem. Nullam maximus libero nec mi tincidunt, sagittis sollicitudin magna semper. Nunc bibendum interdum justo eu convallis. Suspendisse efficitur ligula a mauris consectetur laoreet. Donec vitae erat a dui scelerisque aliquam. Quisque eu dolor sit amet nunc suscipit sagittis. Donec luctus neque sit</p>
    </div>
  </article>

  <article class="article" style="top:676px">
    <div class="article-thumb" role="img" aria-label="Blue sea texture"></div>
    <div class="article-body">
      <h2 class="article-title">LOREM IPSUM DOLOR</h2>
      <p class="article-text">Lorem ipsum dolor sit amet, consectetur adipiscing elit. Etiam accumsan ac erat in consequat. Pellentesque at ligula a lacus elementum pellente&shy;sque nec eget tortor. Maecenas convallis dolor sit amet eros consequat, vitae faucibus arcu pharetra. Quisque vitae fermentum lorem. Nullam maximus libero nec mi tincidunt, sagittis sollicitudin magna semper. Nunc bibendum interdum justo eu convallis. Suspendisse efficitur ligula a mauris consectetur laoreet. Donec vitae erat a dui scelerisque aliquam. Quisque eu dolor sit amet nunc suscipit sagittis. Donec luctus neque sit</p>
    </div>
  </article>

  <article class="article" style="top:888px">
    <div class="article-thumb" role="img" aria-label="Blue sea texture"></div>
    <div class="article-body">
      <h2 class="article-title">LOREM IPSUM DOLOR SIT AMET</h2>
      <p class="article-text">Lorem ipsum dolor sit amet, consectetur adipiscing elit. Etiam accumsan ac erat in consequat. Pellentesque at ligula a lacus elementum pellente&shy;sque nec eget tortor. Maecenas convallis dolor sit amet eros consequat, vitae faucibus arcu pharetra. Quisque vitae fermentum lorem. Nullam maximus libero nec mi tincidunt, sagittis sollicitudin magna semper. Nunc bibendum interdum justo eu convallis. Suspendisse efficitur ligula a mauris consectetur laoreet. Donec vitae erat a dui scelerisque aliquam. Quisque eu dolor sit amet nunc suscipit sagittis. Donec luctus neque sit</p>
    </div>
  </article>

  <footer class="footer-sea" role="img" aria-label="Blue sea band"></footer>

</div>
</body>
</html>
```